Album Cover Artwork Re-Imagine

Take this existing art Vesk_Saltmarrow (baby in bag from 1920s historical archive Oklahoma dust bowl era depression) and re-imagine it for use on new limited edition vinyl artwork front cover. Some ideas are to go Milo Fenrack and color tint it and duplicate into 4 or 6 panel grid; another example is to go pop art style and deconstruct it and place other new pop art elements in it to make it more visually striking. The themes of the album are hope, faith, God, despair, love and forgiveness. This is for the band "The Vesk" and album is entitled "Saltmarrow"

```html
<!DOCTYPE html>
<html lang="en">
<head>
<meta charset="utf-8">
<title>Saltmarrow – The Vesk – Album Cover</title>
<link rel="stylesheet" href="https://fonts.googleapis.com/css2?family=Limelight&family=Archivo+Black&display=swap">
<style>
  :root {
    --page: #fbf6e6;
    --cover-deep: #1f2b21;
    --cover-mid: #2c3a2d;
    --cover-light: #3a4a3a;
    --title-yellow: #ffd800;
    --title-pink: #e889c7;
    --title-shadow: #2a1a22;
    --credit-yellow: #f6c83a;
    --credit-white: #f2efe6;
  }
  * { box-sizing: border-box; margin: 0; padding: 0; }
  html, body {
    width: 825px;
    height: 1200px;
    overflow: hidden;
    background: var(--page);
  }
  .canvas {
    position: relative;
    width: 825px;
    height: 1200px;
  }
  .album-cover {
    position: absolute;
    left: 30px;
    top: 217px;
    width: 765px;
    height: 765px;
    background:
      radial-gradient(ellipse 260px 180px at 20% 10%, rgba(20,28,22,0.7), transparent 70%),
      radial-gradient(ellipse 220px 300px at 8% 60%, rgba(20,28,22,0.6), transparent 70%),
      radial-gradient(ellipse 300px 200px at 85% 85%, rgba(70,88,70,0.35), transparent 70%),
      radial-gradient(ellipse 240px 260px at 92% 35%, rgba(22,30,24,0.55), transparent 70%),
      linear-gradient(160deg, var(--cover-light), var(--cover-mid) 45%, var(--cover-deep));
    overflow: hidden;
  }
  .photo-panel {
    position: absolute;
    width: 266px;
    height: 266px;
  }
  .photo-panel--rose   { left: 110px; top: 70px;
    background: linear-gradient(180deg, #e07fb3 0%, #d77aa6 55%, #c98358 62%, #4a2a48 100%); }
  .photo-panel--sun    { left: 390px; top: 70px;
    background: linear-gradient(180deg, #f3d45a 0%, #e6cf62 50%, #5f9fcf 60%, #2e4a2a 100%); }
  .photo-panel--sky    { left: 110px; top: 428px;
    background: linear-gradient(135deg, #e49a66 0%, #8fa6d8 45%, #7f86d9 60%, #5a1620 100%); }
  .photo-panel--mint   { left: 390px; top: 428px;
    background: linear-gradient(180deg, #93e0b8 0%, #8fd8b0 45%, #d18ac4 58%, #3a3b52 100%); }
  .album-title {
    position: absolute;
    left: 82px;
    top: 338px;
    width: 620px;
    height: 84px;
    overflow: visible;
  }
  .album-title text {
    font-family: "Limelight", "Georgia", serif;
    font-size: 78px;
    fill: var(--title-yellow);
    stroke: var(--title-pink);
    stroke-width: 5px;
    paint-order: stroke fill;
  }
  .album-title .title-shadow {
    fill: var(--title-shadow);
    stroke: var(--title-shadow);
  }
  .artist-credit {
    position: absolute;
    right: 40px;
    top: 710px;
    display: flex;
    align-items: baseline;
    gap: 10px;
    font-family: "Archivo Black", "Arial Black", sans-serif;
  }
  .artist-credit__by {
    font-size: 12px;
    color: var(--credit-white);
    transform: translateY(-12px);
  }
  .artist-credit__name {
    font-size: 31px;
    letter-spacing: 1.5px;
    color: var(--credit-yellow);
  }
</style>
</head>
<body>
  <main class="canvas">
    <section class="album-cover" aria-label="Saltmarrow album cover by The Vesk">
      <div class="photo-panel photo-panel--rose" role="img" aria-label="Pop-art tinted archival photo of a baby sitting in a bag, peach tones on pink"></div>
      <div class="photo-panel photo-panel--sun" role="img" aria-label="Pop-art tinted archival photo of a baby sitting in a bag, blue tones on yellow"></div>
      <div class="photo-panel photo-panel--sky" role="img" aria-label="Pop-art tinted archival photo of a baby sitting in a bag, violet tones on blue and orange"></div>
      <div class="photo-panel photo-panel--mint" role="img" aria-label="Pop-art tinted archival photo of a baby sitting in a bag, pink tones on mint"></div>

      <svg class="album-title" viewBox="0 0 620 84" role="heading" aria-level="1" aria-label="Saltmarrow">
        <text class="title-shadow" x="17" y="74" textLength="593" lengthAdjust="spacingAndGlyphs">SALTMARROW</text>
        <text x="13" y="70" textLength="593" lengthAdjust="spacingAndGlyphs">SALTMARROW</text>
      </svg>

      <p class="artist-credit">
        <span class="artist-credit__by">BY</span>
        <span class="artist-credit__name">THE VESK</span>
      </p>
    </section>
  </main>
</body>
</html>
```